Business card for dental office
Quillbrook Ridge Dental Care
Bright & Fun-filled
18 Larkspur Ln, Suite 310
Dayton, NV 89777
quillbrookridgedentalcare@postmerro.com
quillbrookridgedentalcare.com
Please include website on business card but do not include email address.

```html
<!DOCTYPE html>
<html lang="en">
<head>
<meta charset="utf-8">
<title>Quillbrook Ridge Dental Care – Business Card</title>
<link href="https://fonts.googleapis.com/css2?family=Tinos:wght@400;700&display=swap" rel="stylesheet">
<style>
  :root {
    --backdrop: #8f9092;
    --card-white: #f4f5f6;
    --ink-navy: #24364d;
    --blue-deep: #12506f;
    --blue-bright: #1aa3d9;
    --copper: #a9826a;
    --text-white: #ffffff;
  }
  * { margin: 0; padding: 0; box-sizing: border-box; }
  html, body { width: 1200px; height: 840px; overflow: hidden; }
  body {
    background: var(--backdrop);
    font-family: "Tinos", "Times New Roman", serif;
    position: relative;
  }
  .card {
    position: absolute;
    left: 300px;
    width: 600px;
    height: 343px;
    border-radius: 18px;
    overflow: hidden;
    background: var(--card-white);
    box-shadow: 0 8px 22px rgba(0,0,0,0.28);
  }
  .card--front { top: 48px; }
  .card--back { top: 449px; }

  .brand {
    position: absolute;
    display: flex;
    align-items: center;
    gap: 10px;
    color: var(--ink-navy);
    font-weight: 400;
    text-transform: uppercase;
    letter-spacing: 1px;
  }
  .brand__dot {
    width: 16px; height: 16px; border-radius: 50%;
    background: var(--blue-bright);
    flex: none;
  }
  .card--front .brand {
    top: 118px; left: 0; right: 0;
    justify-content: center;
    font-size: 30px;
  }
  .front__web {
    position: absolute;
    left: 56px; top: 228px;
    font-size: 15px;
    color: var(--blue-deep);
  }

  .back__panel {
    position: absolute;
    left: 0; top: 0;
    width: 232px; height: 100%;
    background: linear-gradient(180deg, var(--blue-deep) 0%, #1780ad 55%, var(--blue-bright) 100%);
    color: var(--text-white);
  }
  .back__divider {
    position: absolute;
    left: 232px; top: 0;
    width: 7px; height: 100%;
    background: var(--copper);
  }
  .back__name {
    position: absolute;
    left: 22px; top: 24px;
    font-size: 15px;
    font-weight: 700;
  }
  .back__address {
    position: absolute;
    left: 22px; top: 120px;
    font-size: 14px;
    line-height: 1.35;
    font-style: normal;
  }
  .back__contacts {
    position: absolute;
    left: 22px; top: 262px;
    list-style: none;
    font-size: 13px;
    line-height: 1.4;
  }
  .back__contacts li { display: flex; align-items: center; gap: 6px; }
  .back__contacts svg { width: 11px; height: 11px; flex: none; }
  .card--back .brand {
    left: 239px; right: 0; top: 150px;
    justify-content: center;
    font-size: 17px;
  }
</style>
</head>
<body>
  <section class="card card--front" aria-label="Card front">
    <div class="brand"><span class="brand__dot"></span><span>Quillbrook Ridge Dental Care</span></div>
    <p class="front__web">www.quillbrookridgedentalcare.com</p>
  </section>

  <section class="card card--back" aria-label="Card back">
    <div class="back__panel">
      <p class="back__name">Quillbrook Ridge Dental Care</p>
      <address class="back__address">18 Larkspur Ln, Suite 310<br>Dayton, NV 89777</address>
      <ul class="back__contacts">
        <li>
          <svg viewBox="0 0 12 12" aria-hidden="true"><path d="M2 1 L4.5 1 L5.5 3.5 L4 4.5 Q5 7 7.5 8 L8.5 6.5 L11 7.5 L11 10 Q6 11 3 8 Q0.5 5 2 1 Z" fill="#fff"/></svg>
          775-555-0142
        </li>
        <li>
          <svg viewBox="0 0 12 12" aria-hidden="true"><rect x="3" y="1" width="6" height="10" rx="1" fill="#fff"/></svg>
          775-555-0187
        </li>
        <li>
          <svg viewBox="0 0 12 12" aria-hidden="true"><circle cx="6" cy="6" r="5" fill="none" stroke="#fff" stroke-width="1.2"/><path d="M1 6 H11 M6 1 Q3 6 6 11 Q9 6 6 1" fill="none" stroke="#fff" stroke-width="0.9"/></svg>
          www.quillbrookridgedentalcare.com
        </li>
      </ul>
    </div>
    <div class="back__divider"></div>
    <div class="brand"><span class="brand__dot"></span><span>Quillbrook Ridge Dental Care</span></div>
  </section>
</body>
</html>
```